Pest Control Company needs business card!

Hi there, we need a business card designed for our new Pest Control Company. Ideally this card will be simple, yet feel elegant and high end. We want to use the colours Orange, Black and White. Please see our attached logo for the exact colours.

Business card details:

Phone - 0461 275 804
Name - Gavin Holloway
Email - Info@steadfastverminguard.com.au

We would also like to include the following list with dot points:

SERVICES / INSPECTIONS

Termites, Wood Borers, Ants, Cockroaches, Spiders, Fleas, Mice, Rats, Bed Bugs, & More!

```html
<!DOCTYPE html>
<html lang="en">
<head>
<meta charset="utf-8">
<title>Steadfast Vermin Guard – Business Card</title>
<link rel="stylesheet" href="https://fonts.googleapis.com/css2?family=Kanit:wght@500;700;800&display=swap">
<style>
  :root {
    --orange: #f2801c;
    --orange-deep: #e46f10;
    --black: #1e1c1c;
    --white: #ffffff;
    --paper: #f7f6f4;
    --backdrop: #2b2e32;
  }
  * { box-sizing: border-box; margin: 0; padding: 0; }
  html, body { width: 1200px; height: 900px; overflow: hidden; }
  body {
    background: var(--backdrop);
    font-family: "Kanit", sans-serif;
    display: flex;
    align-items: center;
    justify-content: center;
    gap: 40px;
  }
  .card {
    position: relative;
    width: 540px;
    height: 330px;
    border-radius: 22px;
    overflow: hidden;
    background: var(--paper);
    box-shadow: 0 14px 30px rgba(0,0,0,.45);
  }
  .card-shapes { position: absolute; inset: 0; }

  /* Info side */
  .services {
    position: absolute;
    left: 30px;
    top: 26px;
    color: var(--black);
  }
  .services-title {
    font-weight: 800;
    font-size: 19px;
    letter-spacing: .5px;
    margin-bottom: 10px;
  }
  .services-list { list-style: none; font-weight: 500; font-size: 15px; line-height: 22px; }
  .services-list li::before {
    content: "";
    display: inline-block;
    width: 0; height: 0;
    border-left: 5px solid transparent;
    border-right: 5px solid transparent;
    border-bottom: 8px solid var(--black);
    margin-right: 8px;
    vertical-align: 2px;
  }
  .contact {
    position: absolute;
    left: 300px;
    right: 8px;
    top: 36px;
    color: var(--white);
  }
  .brand-small {
    display: flex;
    align-items: center;
    gap: 8px;
    font-weight: 700;
    font-size: 14px;
    line-height: 1.05;
    text-transform: uppercase;
    margin-bottom: 22px;
    margin-left: 70px;
  }
  .brand-dot { width: 26px; height: 26px; border-radius: 50%; background: var(--white); flex: none; }
  .person-name {
    font-weight: 700;
    font-size: 24px;
    line-height: 1.1;
    margin-bottom: 18px;
    padding-left: 34px;
    white-space: nowrap;
  }
  .contact-row {
    display: flex;
    align-items: center;
    gap: 6px;
    font-weight: 500;
    font-size: 11px;
    margin-bottom: 9px;
    padding-left: 10px;
    white-space: nowrap;
  }
  .contact-row-phone { padding-left: 22px; }
  .contact-icon { width: 18px; height: 18px; flex: none; }

  /* Logo side */
  .brand-large {
    position: absolute;
    left: 150px;
    top: 50px;
    display: flex;
    align-items: center;
    gap: 16px;
    color: var(--black);
    font-weight: 800;
    font-size: 34px;
    line-height: 1;
    text-transform: uppercase;
  }
  .brand-large-mark { width: 64px; height: 64px; border-radius: 50%; background: var(--black); flex: none; }
</style>
</head>
<body>

  <!-- Info side -->
  <section class="card card-info">
    <svg class="card-shapes" viewBox="0 0 540 330" aria-hidden="true">
      <polygon points="0,0 360,0 215,330 0,330" fill="var(--white)"/>
      <polygon points="360,0 540,0 540,330 215,330" fill="var(--orange)"/>
      <polygon points="346,0 366,0 221,330 188,330" fill="var(--black)"/>
      <polygon points="338,0 343,0 185,330 180,330" fill="var(--white)"/>
      <rect x="0" y="300" width="180" height="30" fill="var(--orange)"/>
    </svg>

    <div class="services">
      <h2 class="services-title">SERIVICES/INSPECTION</h2>
      <ul class="services-list">
        <li>Ants</li>
        <li>Fleas</li>
        <li>Mice</li>
        <li>Rats</li>
        <li>Termites</li>
        <li>Wood Borers</li>
        <li>Cockroaches</li>
        <li>Spiders</li>
        <li>Bed Bugs &amp; More!</li>
      </ul>
    </div>

    <div class="contact">
      <div class="brand-small"><span class="brand-dot"></span><span>Steadfast<br>Vermin Guard</span></div>
      <p class="person-name">Gavin Holloway</p>
      <p class="contact-row contact-row-phone">
        <svg class="contact-icon" viewBox="0 0 22 22" aria-hidden="true">
          <circle cx="11" cy="11" r="11" fill="var(--white)"/>
          <path d="M7.5 6.5c.6-.5 1.3-.4 1.7.2l.9 1.5c.3.5.2 1-.2 1.4l-.6.5c.5 1.2 1.4 2.1 2.6 2.6l.5-.6c.4-.4.9-.5 1.4-.2l1.5.9c.6.4.7 1.1.2 1.7-1 1.1-2.4 1.2-4 .2-1.9-1.1-3.4-2.6-4.4-4.4-.9-1.5-.7-2.9.4-3.8z" fill="var(--orange)"/>
        </svg>
        0461 275 804
      </p>
      <p class="contact-row">
        <svg class="contact-icon" viewBox="0 0 22 22" aria-hidden="true">
          <circle cx="11" cy="11" r="11" fill="var(--white)"/>
          <rect x="5.5" y="7" width="11" height="8" rx="1" fill="var(--orange)"/>
          <path d="M5.8 7.5l5.2 4 5.2-4" stroke="var(--white)" stroke-width="1.2" fill="none"/>
        </svg>
        Info@steadfastverminguard.com.au
      </p>
    </div>
  </section>

  <!-- Logo side -->
  <section class="card card-brand">
    <svg class="card-shapes" viewBox="0 0 540 330" aria-hidden="true">
      <rect x="0" y="0" width="540" height="330" fill="var(--paper)"/>
      <rect x="0" y="206" width="540" height="6" fill="var(--orange)"/>
      <rect x="0" y="222" width="540" height="108" fill="var(--orange)"/>
      <polygon points="118,222 262,222 205,330 118,330" fill="var(--black)"/>
      <polygon points="262,222 272,222 215,330 205,330" fill="var(--white)"/>
    </svg>

    <div class="brand-large">
      <span>Steadfast<br>Vermin<br>Guard</span>
      <span class="brand-large-mark"></span>
    </div>
  </section>

</body>
</html>
```